Board to put on a meditation centre - Lantern Hill Haven

I need a board design for a new meditation centre based in Oslo which offers free courses in meditation and self-empowerment. The size of the board is width 374cm x height 104cm.  The name of the meditation centre together with subtitles should be on the board but also some elegant decoration that matches the theme (lantern hill haven/meditation).
Here is the website of the meditation centre to give you a feeling of it: https://lyktebakkenkurs.no/
Good if you can use a blue color close to this one: rgb(37, 180, 193) as well as some brown/golden color (similar to the palette on the website).
On the board it should say:
Lyktebakken senter (in big letters, the rest is subtitles)
Meditasjon & Spirituell visdom
Kurs - Retreat - Dialog
lyktebakkenkurs.no
The design should be very elegant and beautiful and the feeling should be of "An Lantern Hill Haven". A logo is here attached and should be used but I need to get a better quality version of it, will upload that as soon as possible.

```html
<!DOCTYPE html>
<html lang="no">
<head>
<meta charset="utf-8">
<title>Lyktebakken senter – skilt</title>
<link rel="stylesheet" href="https://fonts.googleapis.com/css2?family=Montserrat:wght@500;600&family=Playfair+Display:ital,wght@1,500&display=swap">
<style>
  :root {
    --page: #ffffff;
    --teal: #25b4c1;
    --ornament-light: rgba(255, 255, 255, 0.42);
    --ornament-soft: rgba(255, 255, 255, 0.16);
    --gold: #f2c230;
    --title-shadow: #137d89;
    --white: #ffffff;
    --ink: #2b2b2b;
    --mark: #d9262e;
    --sky-top: #2f7fd6;
    --sky-mid: #8fc8e6;
    --horizon: #f29a45;
    --sea-top: #2a5f9c;
    --sea-deep: #0d2a52;
  }
  * { margin: 0; padding: 0; box-sizing: border-box; }
  html, body {
    width: 1200px;
    height: 632px;
    overflow: hidden;
    background: var(--page);
  }
  .board {
    position: absolute;
    left: 53px;
    top: 166px;
    width: 1091px;
    height: 303px;
    background: var(--teal);
    overflow: hidden;
  }
  .ornament-area {
    position: absolute;
    left: 0;
    top: 0;
    width: 260px;
    height: 100%;
    background: radial-gradient(ellipse 190px 170px at 0% 50%,
      var(--ornament-light) 0%,
      var(--ornament-soft) 55%,
      rgba(255, 255, 255, 0) 100%);
  }
  .scene-area {
    position: absolute;
    right: 0;
    top: 0;
    width: 470px;
    height: 100%;
    background: linear-gradient(to bottom,
      var(--sky-top) 0%,
      var(--sky-mid) 40%,
      #f6d08a 54%,
      var(--horizon) 57%,
      var(--sea-top) 64%,
      var(--sea-deep) 100%);
    -webkit-mask-image: linear-gradient(to right, transparent 0%, #000 45%);
    mask-image: linear-gradient(to right, transparent 0%, #000 45%);
  }
  .title {
    position: absolute;
    left: 247px;
    width: 600px;
    top: 42px;
    display: flex;
    justify-content: center;
    font-family: "Playfair Display", Georgia, serif;
    font-style: italic;
    font-weight: 500;
    font-size: 74px;
    line-height: 1;
    letter-spacing: 0.5px;
    color: var(--gold);
    text-shadow: 4px 4px 0 var(--title-shadow);
    white-space: nowrap;
  }
  .subtitles {
    position: absolute;
    left: 245px;
    width: 600px;
    top: 155px;
    text-align: center;
    font-family: "Montserrat", Arial, sans-serif;
    font-weight: 600;
    font-size: 26.5px;
    line-height: 30px;
    color: var(--white);
  }
  .site-mark {
    position: absolute;
    left: 440px;
    top: 248px;
    display: flex;
    align-items: center;
    gap: 8px;
  }
  .site-mark__dot {
    width: 32px;
    height: 32px;
    border-radius: 50%;
    background: var(--mark);
  }
  .site-mark__name {
    font-family: "Montserrat", Arial, sans-serif;
    font-weight: 500;
    font-size: 16px;
    color: var(--ink);
  }
</style>
</head>
<body>
  <main class="board">
    <div class="ornament-area" role="img" aria-label="Hvitt mandalamønster som elegant dekor langs venstre kant"></div>
    <div class="scene-area" role="img" aria-label="Solnedgang over stille hav med trinnsteiner og en mediterende silhuett"></div>

    <h1 class="title">Lyktebakken senter</h1>

    <p class="subtitles">
      Meditasjon &amp; Spirituell visdom<br>
      Kurs - Retreat - Dialog
    </p>

    <div class="site-mark">
      <span class="site-mark__dot"></span>
      <span class="site-mark__name">lyktebakkenkurs.no</span>
    </div>
  </main>
</body>
</html>
```